Photography Business, Business Card

Looking for a unique cutting edge card that takes advantage of the latest printing technologies. Please review this site for all the options they office: https://plumeprints.example. If you can think it they can do it. And if you have an idea and do not know if they can do it, I will check into it.
Updates

Target Market(s)

People and places I took images of and future clients.

Industry/Entity Type

Photography

Contact Information for Business Card

Name, cell & email. Derek Hollis, dhollis@kmpvisuals.example, 314-782-0946

Colors

Designer to choose only greyscale colors for use in the design.

Requirements
Must have
• 100% cutting edge. Is so great, those I hand it to always show it to someone else. A piece of art.
Nice to have
• Blacks, silvers, greys, some red. Maybe other colors?

```html
<!DOCTYPE html>
<html lang="en">
<head>
<meta charset="utf-8">
<title>Derek Hollis Photography — Business Card</title>
<link href="https://fonts.googleapis.com/css2?family=Open+Sans:wght@300;400&family=Mrs+Saint+Delafield&display=swap" rel="stylesheet">
<style>
  :root {
    --backdrop: #8c8c8c;
    --card-black: #161616;
    --card-edge: #ee1c25;
    --accent-red: #ee1c25;
    --text-grey: #8a8a8a;
    --signature-grey: #9a9a9a;
    --lens-light: #2b3033;
    --lens-dark: #0d0e0f;
  }
  * { margin: 0; padding: 0; box-sizing: border-box; }
  html, body {
    width: 1200px; height: 1122px; overflow: hidden;
    background: var(--backdrop);
    font-family: "Open Sans", Arial, sans-serif;
  }
  .canvas { position: relative; width: 1200px; height: 1122px; }
  .card { position: absolute; left: 130px; width: 946px; height: 406px; }
  .card--front { top: 110px; }
  .card--back { top: 610px; }
  .card__shape { position: absolute; inset: 0; width: 946px; height: 406px; }
  .card__content { position: absolute; left: 0; top: 0; width: 540px; height: 400px; }

  .brand-name {
    position: absolute; left: 150px; top: 120px;
    font-size: 130px; font-weight: 300; letter-spacing: 6px;
    color: var(--accent-red); line-height: 1;
  }

  .signature {
    position: absolute; left: 50px; top: 50px;
    font-family: "Mrs Saint Delafield", cursive;
    font-size: 96px; color: var(--signature-grey); line-height: 1;
    white-space: nowrap;
  }
  .signature__tagline {
    position: absolute; left: 260px; top: 150px;
    font-size: 14px; letter-spacing: 6px; color: var(--text-grey);
  }
  .contact-icons { position: absolute; left: 70px; top: 200px; display: flex; gap: 8px; }
  .contact-icons svg { width: 30px; height: 30px; }
  .contact-list {
    position: absolute; left: 70px; top: 250px; list-style: none;
    font-size: 22px; font-weight: 300; color: var(--text-grey); line-height: 36px;
    white-space: nowrap;
  }
</style>
</head>
<body>
<main class="canvas">

  <section class="card card--front" aria-label="Card front">
    <svg class="card__shape" viewBox="0 0 946 406">
      <defs>
        <linearGradient id="lens-fill-front" x1="0" y1="0" x2="1" y2="1">
          <stop offset="0" stop-color="var(--lens-light)"/>
          <stop offset="1" stop-color="var(--lens-dark)"/>
        </linearGradient>
      </defs>
      <path d="M26 6 H746 A200 200 0 0 1 746 406 H26 A20 20 0 0 1 6 386 V26 A20 20 0 0 1 26 6 Z" fill="var(--card-edge)"/>
      <path d="M20 0 H740 A200 200 0 0 1 740 400 H20 A20 20 0 0 1 0 380 V20 A20 20 0 0 1 20 0 Z" fill="var(--card-black)"/>
      <circle class="lens-placeholder" role="img" aria-label="Camera lens illustration" cx="740" cy="200" r="196" fill="url(#lens-fill-front)"/>
    </svg>
    <div class="card__content">
      <p class="brand-name">KMP</p>
    </div>
  </section>

  <section class="card card--back" aria-label="Card back">
    <svg class="card__shape" viewBox="0 0 946 406">
      <defs>
        <linearGradient id="lens-fill-back" x1="0" y1="0" x2="1" y2="1">
          <stop offset="0" stop-color="var(--lens-light)"/>
          <stop offset="1" stop-color="var(--lens-dark)"/>
        </linearGradient>
      </defs>
      <path d="M26 6 H746 A200 200 0 0 1 746 406 H26 A20 20 0 0 1 6 386 V26 A20 20 0 0 1 26 6 Z" fill="var(--card-edge)"/>
      <path d="M20 0 H740 A200 200 0 0 1 740 400 H20 A20 20 0 0 1 0 380 V20 A20 20 0 0 1 20 0 Z" fill="var(--card-black)"/>
      <circle class="lens-placeholder" role="img" aria-label="Camera lens illustration" cx="740" cy="200" r="196" fill="url(#lens-fill-back)"/>
    </svg>
    <div class="card__content">
      <p class="signature">Derek Hollis</p>
      <p class="signature__tagline">PHOTOGRAPHY</p>
      <div class="contact-icons">
        <svg viewBox="0 0 30 30" aria-label="Phone">
          <circle cx="15" cy="15" r="15" fill="var(--accent-red)"/>
          <rect x="11" y="7" width="8" height="16" rx="1.5" fill="none" stroke="var(--card-black)" stroke-width="1.8"/>
        </svg>
        <svg viewBox="0 0 30 30" aria-label="Email">
          <circle cx="15" cy="15" r="15" fill="var(--accent-red)"/>
          <rect x="8" y="10" width="14" height="10" fill="none" stroke="var(--card-black)" stroke-width="1.8"/>
          <path d="M8 10 L15 16 L22 10" fill="none" stroke="var(--card-black)" stroke-width="1.8"/>
        </svg>
        <svg viewBox="0 0 30 30" aria-label="Website">
          <circle cx="15" cy="15" r="15" fill="var(--accent-red)"/>
          <circle cx="15" cy="15" r="7" fill="none" stroke="var(--card-black)" stroke-width="1.8"/>
          <path d="M8 15 H22 M15 8 C11 12 11 18 15 22 C19 18 19 12 15 8" fill="none" stroke="var(--card-black)" stroke-width="1.5"/>
        </svg>
      </div>
      <ul class="contact-list">
        <li>314-782-0946</li>
        <li>dhollis@kmpvisuals.example</li>
        <li>www.kmpvisuals.example</li>
      </ul>
    </div>
  </section>

</main>
</body>
</html>
```